Book Cover - for a Murder book

PROJECT DEADLINE JAN 6TH END OF DAY (Seattle Time).
Goal of the project is to design a book cover for a book related to the investigation of the murder of the Mexican presidential candidate Ramiro Esteban Vallarta.
Look at presidential assassination books in Quillora for ideas.
Also look at pictures in the web of Ramiro Esteban Vallarta, for example here:
http://www.fotobuscador-demo.net/images/search?q=ramiro+esteban+vallarta&FORM=HDRSC2
Must deliver in format that can be modified (either PSD or Illustrator), as well as in PNG.
The author of the book is the most important lawyer in Mexico, so the cover should show that this book is serious, interesting, deep, to be trusted.
Image should contain:
Image: 1563 pixels x 2500 pixels (front page)
- and extend the design to cover the side of the book and the back of the book
Back of the book: a placeholder for a small title, a picture of the author, and a few lines of text
Title of the book: Testigo Nueve
Subtitle (smaller font): El asesinato de Ramiro Esteban Vallarta
Author: Dr. Martín Olvera Quintana
I will also create a version in English, changing the text to:
Title of the Book: Witness Nine
Subtitle (smaller font): The assasination of Ramiro Esteban Vallarta
Hi, we've received many great designs, so we have more than enough. We will be making the decision tomorrow, January 6th, end of day.
Target Market(s)
Serious readers of investigative murders.
Industry/Entity Type
Lawyer
Look and feel

```html
<!DOCTYPE html>
<html lang="es">
<head>
<meta charset="utf-8">
<title>Testigo Nueve — Portada</title>
<link href="https://fonts.googleapis.com/css2?family=Roboto+Condensed:wght@400;700;800&display=swap" rel="stylesheet">
<style>
  :root {
    --stage: #e4e4e4;
    --cover-black: #0c0c0c;
    --title-white: #f0f0f0;
    --band-white: #ececec;
    --title-red: #a3161b;
    --target-red: #8e1518;
    --subtitle-grey: #3a3a3a;
    --name-green: #1d6b2a;
    --photo-dark: #2a2a2a;
    --photo-light: #8a8a8a;
  }
  * { margin: 0; padding: 0; box-sizing: border-box; }
  html, body {
    width: 1200px; height: 900px; overflow: hidden;
    background: var(--stage);
  }
  .stage {
    width: 1200px; height: 900px;
    display: flex; align-items: center; justify-content: center;
  }
  .cover {
    position: relative;
    width: 562px; height: 900px;
    background: var(--cover-black);
    font-family: "Roboto Condensed", "Arial Narrow", sans-serif;
    overflow: hidden;
  }
  .title-top {
    position: absolute; left: 68px; top: 62px;
    font-size: 100px; font-weight: 800; line-height: 1;
    color: var(--title-white); letter-spacing: 1px;
  }
  .title-band {
    position: absolute; left: 0; top: 157px;
    width: 412px; height: 93px;
    background: var(--band-white);
  }
  .title-bottom {
    position: absolute; left: 68px; top: 150px;
    font-size: 106px; font-weight: 800; line-height: 1;
    color: var(--title-red); letter-spacing: 1px;
  }
  .portrait {
    position: absolute; left: 55px; top: 285px;
    width: 425px; height: 410px;
    background: radial-gradient(ellipse at 55% 45%, var(--photo-light) 0%, var(--photo-dark) 60%, var(--cover-black) 100%);
  }
  .target {
    position: absolute; left: 196px; top: 308px;
    width: 208px; height: 208px;
  }
  .subtitle-band {
    position: absolute; left: 0; top: 697px;
    width: 100%; height: 74px;
    background: var(--band-white);
    display: flex; align-items: center; justify-content: center;
    font-size: 28px; white-space: nowrap;
  }
  .subtitle-lead { color: var(--subtitle-grey); font-weight: 400; margin-right: 8px; }
  .subtitle-name { color: var(--name-green); font-weight: 700; }
  .author {
    position: absolute; left: 0; top: 838px; width: 100%;
    text-align: center; font-size: 24px; color: var(--title-white);
  }
</style>
</head>
<body>
  <main class="stage">
    <article class="cover">
      <h1 class="title">
        <span class="title-top">TESTIGO</span>
        <span class="title-band"></span>
        <span class="title-bottom">NUEVE</span>
      </h1>
      <div class="portrait" role="img" aria-label="Fotografía en blanco y negro de Ramiro Esteban Vallarta de perfil, hablando con la mano extendida"></div>
      <svg class="target" viewBox="0 0 208 208" aria-hidden="true">
        <g fill="none" stroke="var(--target-red)" stroke-width="8">
          <circle cx="104" cy="104" r="98"/>
          <circle cx="104" cy="104" r="62"/>
          <line x1="104" y1="2" x2="104" y2="80"/>
          <line x1="104" y1="128" x2="104" y2="206"/>
          <line x1="2" y1="104" x2="80" y2="104"/>
          <line x1="128" y1="104" x2="206" y2="104"/>
        </g>
      </svg>
      <p class="subtitle-band">
        <span class="subtitle-lead">El asesinato de</span>
        <span class="subtitle-name">Ramiro Esteban Vallarta</span>
      </p>
      <p class="author">Dr. Martín Olvera Quintana</p>
    </article>
  </main>
</body>
</html>
```